Lumora Business Card Design

hello,
we are looking for a business card design for our Fintech Company. We are credit card processing company that is also expanding in to the crypto market. We will be focusing on crypto processing, with a crypto wallet and crypto exchange. We like the purple in the logo. We want something modern and sophisticated but at the same time simple and trust worthy to work with banks.

Industry/Entity Type

Fintech

Logo Text

Lumora

```html
<!DOCTYPE html>
<html lang="en">
<head>
<meta charset="utf-8">
<title>Lumora Business Card</title>
<link rel="stylesheet" href="https://fonts.googleapis.com/css2?family=Montserrat:wght@500;600&family=Arimo:wght@700&display=swap">
<style>
  :root {
    --backdrop: #939a99;
    --card-light: #ffffff;
    --card-dark: #2d1847;
    --brand-purple: #4a3bc4;
    --brand-navy: #25305a;
    --edge-blue: #1a4fa0;
    --teal: #28b3c8;
    --ocean: #0f5fb0;
    --icon-white: #ffffff;
  }
  html, body {
    margin: 0;
    padding: 0;
    width: 1200px;
    height: 1200px;
    overflow: hidden;
    background: var(--backdrop);
  }
  .gradient-defs { position: absolute; width: 0; height: 0; }
  .business-card {
    position: absolute;
    left: 148px;
    width: 904px;
    height: 304px;
    display: block;
  }
  .card-light { top: 268px; }
  .card-dark { top: 628px; }
  .card-light .card-face, .card-light .logo-disc { fill: var(--card-light); }
  .card-dark .card-face, .card-dark .logo-disc { fill: var(--card-dark); }
  .edge-line { fill: none; stroke: var(--edge-blue); stroke-width: 3; }
  .brand-name {
    font-family: "Montserrat", sans-serif;
    font-weight: 500;
    font-size: 26px;
    letter-spacing: 0.5px;
    fill: var(--brand-navy);
  }
  .logo-name {
    font-family: "Montserrat", sans-serif;
    font-weight: 600;
    font-size: 24px;
    fill: var(--brand-purple);
  }
  .job-title {
    font-family: "Montserrat", sans-serif;
    font-weight: 500;
    font-size: 15px;
    fill: var(--brand-purple);
  }
  .title-rule { stroke: var(--ocean); stroke-width: 1.5; }
  .contact-pill { fill: var(--brand-purple); }
  .contact-line {
    font-family: "Arimo", sans-serif;
    font-weight: 700;
    font-size: 15px;
    fill: var(--brand-purple);
  }
  .contact-icon { fill: none; stroke: var(--icon-white); stroke-width: 1.3; stroke-linecap: round; stroke-linejoin: round; }
  .contact-icon-solid { fill: var(--icon-white); }
  .social-tile { fill: var(--icon-white); }
</style>
</head>
<body>

<svg class="gradient-defs" aria-hidden="true">
  <defs>
    <linearGradient id="side-band" x1="0" y1="0" x2="1" y2="0">
      <stop offset="0" stop-color="var(--ocean)"/>
      <stop offset="1" stop-color="var(--teal)"/>
    </linearGradient>
    <linearGradient id="corner-arc" x1="0" y1="0" x2="1" y2="0.4">
      <stop offset="0" stop-color="var(--teal)"/>
      <stop offset="1" stop-color="var(--ocean)"/>
    </linearGradient>
  </defs>
</svg>

<svg class="business-card card-light" viewBox="0 0 678 228" aria-label="Lumora business card, light version">
  <rect width="678" height="228" fill="url(#side-band)"/>
  <path class="edge-line" d="M155,0 C181,80 171,160 191,228"/>
  <path class="card-face" d="M159,0 C185,80 175,160 195,228 L678,228 L678,0 Z"/>
  <path d="M519,0 C540,70 610,100 678,100 L678,0 Z" fill="url(#corner-arc)"/>
  <circle class="logo-disc" cx="172" cy="128" r="67"/>
  <text class="logo-name" x="172" y="136" text-anchor="middle">Lumora</text>

  <g class="social-links">
    <rect class="social-tile" x="572" y="22" width="17" height="17" rx="2"/>
    <rect class="social-tile" x="598" y="22" width="17" height="17" rx="8.5"/>
    <rect class="social-tile" x="624" y="22" width="17" height="17" rx="2"/>
  </g>

  <text class="brand-name" x="266" y="42">LUMORA</text>
  <text class="job-title" x="283" y="63">CEO / Founder</text>
  <line class="title-rule" x1="281" y1="68" x2="397" y2="68"/>

  <rect class="contact-pill" x="270" y="87" width="24" height="92" rx="12"/>
  <path class="contact-icon" d="M277,97 q1,-2 3,0 l1,2 q0,1 -1,2 q1,3 4,4 q1,-1 2,-1 l2,1 q2,2 0,3 q-6,1 -11,-11 z"/>
  <circle class="contact-icon" cx="282" cy="123" r="5"/>
  <path class="contact-icon" d="M277,123 h10 M282,118 q-3,5 0,10 q3,-5 0,-10"/>
  <rect class="contact-icon" x="277" y="139" width="10" height="7"/>
  <path class="contact-icon" d="M277,139 l5,4 l5,-4"/>
  <path class="contact-icon-solid" d="M282,171 c-4,-5 -5,-7 -5,-9 a5,5 0 0 1 10,0 c0,2 -1,4 -5,9 z"/>
  <circle cx="282" cy="162" r="2" fill="var(--brand-purple)"/>

  <text class="contact-line" x="302" y="105">+41 3100 7284</text>
  <text class="contact-line" x="304" y="128">lumorapay.com</text>
  <text class="contact-line" x="304" y="147">www.lumorapay.com</text>
  <text class="contact-line" x="302" y="170">Lindenweg 8</text>
</svg>

<svg class="business-card card-dark" viewBox="0 0 678 228" aria-label="Lumora business card, dark version">
  <rect width="678" height="228" fill="url(#side-band)"/>
  <path class="edge-line" d="M155,0 C181,80 171,160 191,228"/>
  <path class="card-face" d="M159,0 C185,80 175,160 195,228 L678,228 L678,0 Z"/>
  <path d="M519,0 C540,70 610,100 678,100 L678,0 Z" fill="url(#corner-arc)"/>
  <circle class="logo-disc" cx="172" cy="124" r="67"/>
  <text class="logo-name" x="172" y="132" text-anchor="middle">Lumora</text>

  <g class="social-links">
    <rect class="social-tile" x="572" y="22" width="17" height="17" rx="2"/>
    <rect class="social-tile" x="598" y="22" width="17" height="17" rx="8.5"/>
    <rect class="social-tile" x="624" y="22" width="17" height="17" rx="2"/>
  </g>

  <text class="brand-name" x="266" y="49">LUMORA</text>
  <text class="job-title" x="283" y="69">CEO / Founder</text>
  <line class="title-rule" x1="281" y1="74" x2="397" y2="74"/>

  <rect class="contact-pill" x="270" y="94" width="24" height="92" rx="12"/>
  <path class="contact-icon" d="M277,103 q1,-2 3,0 l1,2 q0,1 -1,2 q1,3 4,4 q1,-1 2,-1 l2,1 q2,2 0,3 q-6,1 -11,-11 z"/>
  <circle class="contact-icon" cx="282" cy="130" r="5"/>
  <path class="contact-icon" d="M277,130 h10 M282,125 q-3,5 0,10 q3,-5 0,-10"/>
  <rect class="contact-icon" x="277" y="146" width="10" height="7"/>
  <path class="contact-icon" d="M277,146 l5,4 l5,-4"/>
  <path class="contact-icon-solid" d="M282,177 c-4,-5 -5,-7 -5,-9 a5,5 0 0 1 10,0 c0,2 -1,4 -5,9 z"/>
  <circle cx="282" cy="168" r="2" fill="var(--brand-purple)"/>

  <text class="contact-line" x="302" y="112">+41 3100 7284</text>
  <text class="contact-line" x="304" y="134">lumorapay.com</text>
  <text class="contact-line" x="304" y="153">www.lumorapay.com</text>
  <text class="contact-line" x="302" y="176">Lindenweg 8</text>
</svg>

</body>
</html>
```